Looking for awesome business card design with attached existing logo

We are a water, mold, and fire damage restoration company called "Torvane Seco" Looking for an awesome business card that is edgy yet professional and unique. Show me what you got!

```html
<!DOCTYPE html>
<html lang="en">
<head>
<meta charset="utf-8">
<title>Torvane Seco — Business Card</title>
<link href="https://fonts.googleapis.com/css2?family=Open+Sans:wght@400;700&display=swap" rel="stylesheet">
<style>
  :root {
    --stage: #000000;
    --paper: #ffffff;
    --navy: #314d58;
    --gold: #d4992e;
    --ink: #1e1e1e;
  }
  * { margin: 0; padding: 0; box-sizing: border-box; }
  html, body {
    width: 1200px; height: 1200px; overflow: hidden;
    background: var(--stage);
    font-family: "Open Sans", sans-serif;
  }
  .card {
    position: absolute; left: 220px; width: 754px; height: 431px;
    background: var(--paper); overflow: hidden;
  }
  .card-front { top: 144px; }
  .card-back { top: 620px; }

  .brand-name {
    position: absolute; font-weight: 700; color: var(--navy);
    white-space: nowrap; display: flex; align-items: center;
  }
  .brand-name .brand-dot {
    display: inline-block; border-radius: 50%; background: var(--gold);
  }
  .card-front .brand-name {
    left: 0; right: 0; top: 170px; justify-content: center;
    font-size: 72px; gap: 22px;
  }
  .card-front .brand-dot { width: 26px; height: 26px; }
  .card-back .brand-name {
    left: 26px; top: 118px; font-size: 38px; gap: 12px;
  }
  .card-back .brand-dot { width: 14px; height: 14px; }

  .person {
    position: absolute; right: 30px; top: 40px; text-align: right;
  }
  .person-name { font-size: 31px; font-weight: 700; line-height: 1.15; }
  .person-name .first { color: var(--gold); }
  .person-name .last { color: var(--navy); }
  .person-title { font-size: 21px; color: var(--ink); margin-top: 4px; }
  .accent-bar {
    position: absolute; right: 0; top: 44px; width: 21px; height: 59px;
    background: var(--gold);
  }

  .contact-band {
    position: absolute; left: 0; right: 0; top: 233px; bottom: 0;
    background: var(--gold);
  }
  .navy-block {
    position: absolute; left: 615px; right: 0; top: 0; bottom: 0;
    background: var(--navy);
  }
  .band-circle {
    position: absolute; left: 542px; top: 38px; width: 120px; height: 120px;
    border-radius: 50%; background: var(--paper);
  }
  .address {
    position: absolute; left: 27px; top: 18px;
    color: var(--paper); font-size: 21px; line-height: 26px;
  }
  .contact-list {
    position: absolute; left: 27px; top: 88px; list-style: none;
    color: var(--paper); font-size: 20px;
  }
  .contact-list li {
    display: flex; align-items: center; height: 27px; gap: 12px;
  }
  .contact-list svg { width: 18px; height: 18px; flex: none; }
</style>
</head>
<body>
  <section class="card card-front">
    <div class="brand-name"><span class="brand-dot"></span>Torvane Seco</div>
  </section>

  <section class="card card-back">
    <div class="brand-name"><span class="brand-dot"></span>Torvane Seco</div>

    <div class="accent-bar"></div>
    <div class="person">
      <p class="person-name"><span class="first">Mirela</span> <span class="last">Vostek</span></p>
      <p class="person-title">Managing Director</p>
    </div>

    <div class="contact-band">
      <div class="navy-block"></div>
      <div class="band-circle"></div>
      <p class="address">1840 Halden Ave. Suite<br>300 Granford, TX 76540</p>
      <ul class="contact-list">
        <li>
          <svg viewBox="0 0 24 24" fill="#fff"><path d="M6.6 10.8a15 15 0 0 0 6.6 6.6l2.2-2.2a1 1 0 0 1 1-.25 11.4 11.4 0 0 0 3.6.57 1 1 0 0 1 1 1V20a1 1 0 0 1-1 1A17 17 0 0 1 3 4a1 1 0 0 1 1-1h3.5a1 1 0 0 1 1 1c0 1.25.2 2.45.57 3.57a1 1 0 0 1-.25 1z"/></svg>
          (555) 214-0387
        </li>
        <li>
          <svg viewBox="0 0 24 24" fill="none" stroke="#fff" stroke-width="2"><rect x="3" y="6" width="18" height="13" rx="1"/><path d="M3 7l9 7 9-7"/></svg>
          hello@torvaneseco.com
        </li>
        <li>
          <svg viewBox="0 0 24 24" fill="none" stroke="#fff" stroke-width="2"><circle cx="12" cy="12" r="9"/><path d="M3 12h18M12 3c3 3 3 15 0 18M12 3c-3 3-3 15 0 18"/></svg>
          www.torvaneseco.com
        </li>
      </ul>
    </div>
  </section>
</body>
</html>
```